Harbrook Builders PowerPoint Presentation

We need a sales pitch in powerpoint form for a "commercial only" construction company based out of Dallas, TX. We perform commercial only construction including ground up, build to suit, white box and many others. We would like the design to match the color scheme and outlook of the website and brochure that will be attached. Also, attached you will find the old presentation we used (it's terrible). http://www.harbrookbld.example/

Target Market(s)

Commercial property managers, commercial building owners, business owners, facility managers, commercial construction managers, construction design teams

Industry/Entity Type

Construction

Requirements
Must have
• Commercial construction pictures. Company overview. Specific industries served.
Should not have
• Residential pictures. Poor quality pictures. Anything that doesn't look like the website or attached brochure.

```html
<!DOCTYPE html>
<html lang="en">
<head>
<meta charset="utf-8">
<title>Harbrook Builders Presentation</title>
<link rel="stylesheet" href="https://fonts.googleapis.com/css2?family=Open+Sans:wght@400;600;700&display=swap">
<style>
  :root {
    --orange: #d9782c;
    --ink: #1e1e1e;
    --charcoal: #3b3b3b;
    --slate: #555759;
    --paper: #ffffff;
    --page-bg: #ffffff;
    --muted: #8a8a8a;
  }
  * { box-sizing: border-box; margin: 0; padding: 0; }
  html, body { width: 800px; height: 1200px; overflow: hidden; background: var(--page-bg); }
  body { position: relative; font-family: "Open Sans", sans-serif; color: var(--ink); }

  .slide {
    position: absolute; left: 145px; width: 510px; height: 270px;
    background: var(--paper); overflow: hidden;
    box-shadow: 0 2px 6px rgba(0,0,0,.35);
  }
  .slide--title { top: 30px; }
  .slide--mission { top: 322px; }
  .slide--services { top: 614px; }
  .slide--clients { top: 906px; }

  .top-tab { position: absolute; top: 0; width: 30px; height: 4px; background: var(--ink); }

  .brand { position: absolute; display: flex; align-items: center; gap: 5px; }
  .brand-mark { width: 11px; height: 11px; background: var(--orange); }
  .brand-name { font-weight: 700; font-size: 15px; color: var(--ink); letter-spacing: .5px; }
  .brand--small .brand-mark { width: 7px; height: 7px; }
  .brand--small .brand-name { font-size: 9px; }

  .photo { position: absolute; }

  /* Title slide */
  .slide--title .top-tab { left: 70px; }
  .slide--title .brand { left: 16px; top: 12px; }
  .title-photo { left: 0; top: 36px; width: 510px; height: 196px;
    background: linear-gradient(120deg, #9a9a9a 0%, #5c5c5c 35%, #3a3a3a 60%, #2b2b2b 100%); }
  .title-heading { position: absolute; right: 24px; top: 96px; color: var(--paper);
    font-size: 27px; font-weight: 400; letter-spacing: .5px; }
  .title-sub { position: absolute; right: 24px; top: 134px; color: #e6e6e6; font-size: 10px; }
  .title-url { position: absolute; right: 14px; bottom: 12px; color: var(--orange); font-size: 7px; }

  /* Mission slide */
  .slide--mission .top-tab { left: 200px; }
  .mission-photo { left: 0; top: 0; width: 245px; height: 236px;
    background: linear-gradient(160deg, #f1f1f1 0%, #c9c9c9 45%, #8f8f8f 100%); }
  .section-heading { position: absolute; color: var(--orange); font-size: 17px; font-weight: 400; letter-spacing: .3px; }
  .slide--mission .section-heading { left: 232px; top: 16px; }
  .mission-box { position: absolute; left: 148px; top: 52px; width: 208px; height: 150px;
    background: var(--charcoal); color: var(--paper); font-size: 11px; line-height: 1.35;
    text-align: center; display: flex; align-items: center; padding: 12px 18px; }

  .footer-note { position: absolute; bottom: 12px; right: 48px; font-size: 4.5px; color: var(--muted); }
  .page-num { position: absolute; bottom: 8px; right: 16px; width: 13px; height: 13px; border-radius: 50%;
    background: var(--orange); color: var(--paper); font-size: 6px; display: flex; align-items: center; justify-content: center; }
  .slide .brand--small { left: 14px; bottom: 9px; }

  /* Services slide */
  .slide--services .top-tab, .slide--clients .top-tab { left: 14px; }
  .slide--services .section-heading, .slide--clients .section-heading { left: 14px; top: 12px; }
  .dark-band { position: absolute; left: 0; width: 510px; background: var(--slate); }
  .slide--services .dark-band { top: 52px; height: 180px; }
  .service-grid { position: absolute; left: 0; top: 52px; width: 510px; height: 180px;
    display: grid; grid-template-columns: repeat(3, 1fr); grid-template-rows: repeat(2, 1fr); gap: 4px; padding: 4px 70px; }
  .service-tile { position: relative; }
  .service-tile .photo { inset: 0 0 14px 0; }
  .tile-label { position: absolute; left: 0; right: 0; bottom: 2px; text-align: center; color: var(--paper); font-size: 6.5px; }
  .tone-a { background: linear-gradient(150deg, #7d8fa4, #404a55); }
  .tone-b { background: linear-gradient(150deg, #6c7d8e, #2e3640); }
  .tone-c { background: linear-gradient(150deg, #b7b9bb, #6b6f73); }
  .tone-d { background: linear-gradient(150deg, #7b8a5f, #3c4433); }
  .tone-e { background: linear-gradient(150deg, #8d8d8d, #3d3d3d); }
  .tone-f { background: linear-gradient(150deg, #4f6a8c, #22324a); }

  /* Clients slide */
  .slide--clients .dark-band { top: 52px; height: 184px; background: var(--charcoal); }
  .client-row { position: absolute; left: 0; top: 100px; width: 510px; display: flex; justify-content: center; gap: 10px; }
  .client-card { width: 98px; }
  .client-card .photo { position: relative; height: 62px; }
  .client-card .tile-label { position: static; margin-top: 6px; font-size: 7px; }
  .tone-g { background: linear-gradient(160deg, #f1ece4, #b9ad9c); }
  .tone-h { background: linear-gradient(160deg, #9fb3c9, #8a6a4c); }
  .tone-i { background: linear-gradient(160deg, #c4975c, #3d2b1d); }
</style>
</head>
<body>

<section class="slide slide--title">
  <div class="top-tab"></div>
  <div class="brand"><span class="brand-mark"></span><span class="brand-name">HARBROOK</span></div>
  <div class="photo title-photo" role="img" aria-label="Commercial building under construction, steel framing in grey tones"></div>
  <h1 class="title-heading">YOUR TITLE HERE</h1>
  <p class="title-sub">Your Subtitle Here</p>
  <p class="title-url">www.harbrookbld.example</p>
</section>

<section class="slide slide--mission">
  <div class="top-tab"></div>
  <div class="photo mission-photo" role="img" aria-label="Bright open commercial interior with exposed ceiling"></div>
  <h2 class="section-heading">MISSON STATEMENT</h2>
  <p class="mission-box">It is Our mission to provide the highest quality of service in all aspects of our business; to fulfill these responsibilities while maintaining the highest ethical standards in both our work, and our character</p>
  <p class="footer-note">Copyright Harbrook Builders. All rights reserved.</p>
  <div class="page-num">2</div>
</section>

<section class="slide slide--services">
  <div class="top-tab"></div>
  <h2 class="section-heading">SERVICE WE PROVIDE</h2>
  <div class="dark-band"></div>
  <div class="service-grid">
    <div class="service-tile"><div class="photo tone-a" role="img" aria-label="Roofing crew on a commercial roof"></div><span class="tile-label">Roofing</span></div>
    <div class="service-tile"><div class="photo tone-b" role="img" aria-label="Rooftop HVAC units"></div><span class="tile-label">HVAC</span></div>
    <div class="service-tile"><div class="photo tone-c" role="img" aria-label="Empty commercial space ready for trade out"></div><span class="tile-label">General Trade Out</span></div>
    <div class="service-tile"><div class="photo tone-d" role="img" aria-label="Exterior wall and siding work"></div><span class="tile-label">Exterior Work</span></div>
    <div class="service-tile"><div class="photo tone-e" role="img" aria-label="Fire damaged interior being restored"></div><span class="tile-label">Fire Restoration</span></div>
    <div class="service-tile"><div class="photo tone-f" role="img" aria-label="Emergency water cleanup equipment"></div><span class="tile-label">Emergency Services</span></div>
  </div>
  <div class="brand brand--small"><span class="brand-mark"></span><span class="brand-name">HARBROOK</span></div>
  <p class="footer-note">Copyright Harbrook Builders. All rights reserved.</p>
  <div class="page-num">3</div>
</section>

<section class="slide slide--clients">
  <div class="top-tab"></div>
  <h2 class="section-heading">WHO WE SERVICE</h2>
  <div class="dark-band"></div>
  <div class="client-row">
    <div class="client-card"><div class="photo tone-g" role="img" aria-label="Multi family building interior"></div><p class="tile-label">Multi Family</p></div>
    <div class="client-card"><div class="photo tone-h" role="img" aria-label="Retail storefront building"></div><p class="tile-label">Retail</p></div>
    <div class="client-card"><div class="photo tone-i" role="img" aria-label="Commercial lobby interior"></div><p class="tile-label">Commercial</p></div>
  </div>
  <div class="brand brand--small"><span class="brand-mark"></span><span class="brand-name">HARBROOK</span></div>
  <p class="footer-note">Copyright Harbrook Builders. All rights reserved.</p>
  <div class="page-num">4</div>
</section>

</body>
</html>
```